Business Card For Kelmora Financial Consulting

Hi, I would like a business card designed. Bold, modern.
Please use the same design as the logo. I have also attached the website design to see the overall theme.
Wordmark Font
Color: Hex: #01AEF7

```html
<!DOCTYPE html>
<html lang="en">
<head>
<meta charset="utf-8">
<title>Kelmora Financial Consulting – Business Card</title>
<link rel="stylesheet" href="https://fonts.googleapis.com/css2?family=Montserrat:wght@300;400;600;700&display=swap">
<style>
  :root {
    --page-bg: #e8e8e8;
    --card-navy: #16212b;
    --brand-blue: #45b0e5;
    --paper-white: #ffffff;
    --text-light: #d9dde1;
  }
  * { margin: 0; padding: 0; box-sizing: border-box; }
  html, body {
    width: 1200px; height: 1200px; overflow: hidden;
    background: var(--page-bg);
    font-family: "Montserrat", Arial, sans-serif;
  }
  .card {
    position: absolute; left: 150px;
    width: 900px; height: 530px;
    background: var(--card-navy);
    overflow: hidden;
    box-shadow: 0 4px 10px rgba(0,0,0,0.22);
  }
  .card--front { top: 59px; }
  .card--back  { top: 615px; }
  .card__shapes { position: absolute; inset: 0; width: 900px; height: 530px; }

  .wordmark {
    position: absolute;
    color: var(--paper-white);
    font-weight: 600;
    line-height: 1;
    text-transform: uppercase;
  }
  .wordmark__line { display: block; white-space: nowrap; }

  .card--front .wordmark { left: 75px; top: 96px; }
  .card--front .wordmark__main { font-size: 38px; letter-spacing: 1.5px; }
  .card--front .wordmark__sub { font-size: 11px; letter-spacing: 3.6px; margin-top: 7px; }

  .card--back .wordmark { left: 266px; top: 352px; }
  .card--back .wordmark__main { font-size: 60px; letter-spacing: 2.5px; }
  .card--back .wordmark__sub { font-size: 17px; letter-spacing: 6.2px; margin-top: 10px; }

  .holder { position: absolute; left: 76px; top: 290px; }
  .holder__name { font-size: 30px; font-weight: 700; color: var(--paper-white); }
  .holder__role { font-size: 21px; font-weight: 300; color: var(--text-light); margin-top: 2px; }

  .contacts { position: absolute; right: 55px; top: 300px; list-style: none; }
  .contacts__item {
    display: flex; justify-content: flex-end; align-items: flex-start; gap: 14px;
    font-size: 21px; font-weight: 300; color: var(--paper-white);
    text-align: right; line-height: 29px; margin-bottom: 14px;
  }
  .contacts__icon { width: 18px; height: 18px; margin-top: 6px; flex: none; }
</style>
</head>
<body>

<section class="card card--front" aria-label="Business card front">
  <svg class="card__shapes" viewBox="0 0 720 424" preserveAspectRatio="none" aria-hidden="true">
    <rect x="258" y="408" width="160" height="160" rx="22" transform="rotate(45 338 488)" fill="var(--paper-white)"/>
    <rect x="650" y="420" width="110" height="110" rx="16" transform="rotate(45 705 475)" fill="var(--paper-white)"/>
    <rect x="368" y="159" width="318" height="318" rx="32" transform="rotate(45 527 318)" fill="var(--brand-blue)"/>
    <rect x="520" y="-89" width="145" height="145" rx="14" transform="rotate(45 592 -17)" fill="var(--brand-blue)"/>
  </svg>

  <div class="wordmark">
    <span class="wordmark__line wordmark__main">Kelmora</span>
    <span class="wordmark__line wordmark__sub">Financial Consulting</span>
  </div>

  <div class="holder">
    <p class="holder__name">Daniel Ruiz</p>
    <p class="holder__role">Practitioner</p>
  </div>

  <ul class="contacts">
    <li class="contacts__item">416-555-0142
      <svg class="contacts__icon" viewBox="0 0 24 24" aria-hidden="true"><path d="M6.6 2.5l3 .6 1.2 4.2-2.2 1.7a12 12 0 0 0 6.4 6.4l1.7-2.2 4.2 1.2.6 3-2.4 2.4C12 19.6 4.4 12 3.9 4.9z" fill="none" stroke="#fff" stroke-width="2" stroke-linejoin="round"/></svg>
    </li>
    <li class="contacts__item">hello@kelmora.com
      <svg class="contacts__icon" viewBox="0 0 24 24" aria-hidden="true"><circle cx="12" cy="12" r="9.5" fill="none" stroke="#fff" stroke-width="2"/><path d="M3 12h18M12 2.5c3 3 3 16 0 19M12 2.5c-3 3-3 16 0 19" fill="none" stroke="#fff" stroke-width="1.6"/></svg>
    </li>
    <li class="contacts__item"><span>120 Harbour Lane, Suite 210,<br>Toronto, M5V 2K4</span>
      <svg class="contacts__icon" viewBox="0 0 24 24" aria-hidden="true"><path d="M12 2a6 6 0 0 0-6 6c0 4.5 6 10 6 10s6-5.5 6-10a6 6 0 0 0-6-6z" fill="none" stroke="#fff" stroke-width="2"/><circle cx="12" cy="8" r="2" fill="#fff"/><path d="M5 21h14" stroke="#fff" stroke-width="2"/></svg>
    </li>
  </ul>
</section>

<section class="card card--back" aria-label="Business card back">
  <svg class="card__shapes" viewBox="0 0 720 424" preserveAspectRatio="none" aria-hidden="true">
    <rect x="15" y="-39" width="210" height="210" rx="20" transform="rotate(45 120 66)" fill="var(--paper-white)"/>
    <rect x="166" y="106" width="84" height="84" rx="14" transform="rotate(45 208 148)" fill="var(--brand-blue)"/>
    <rect x="334" y="-103" width="192" height="192" rx="18" transform="rotate(45 430 -7)" fill="none" stroke="var(--paper-white)" stroke-width="1.6"/>
  </svg>

  <div class="wordmark">
    <span class="wordmark__line wordmark__main">Kelmora</span>
    <span class="wordmark__line wordmark__sub">Financial Consulting</span>
  </div>
</section>

</body>
</html>
```